General Contractor Marketing Flyer

Need a flyer to hand out at trade show directed towards craft breweries and restaurants. We are a General Contractor that builds projects for industry. We also can provide design services when requested.
We are located in Chicago, IL and work throughout the US. Would like to see a design that emphasizes our expertise and knowledge within the Hospitality industry. We are including our logo and some previous work experience. Our website is www.larkmeadbuild.com for further information

```html
<!DOCTYPE html>
<html lang="en">
<head>
<meta charset="utf-8">
<title>Larkmead Design + Build — Hospitality Flyer</title>
<link href="https://fonts.googleapis.com/css2?family=Poppins:wght@400;500;600;700&display=swap" rel="stylesheet">
<style>
  :root{
    --navy:#323a69;
    --paper:#ffffff;
    --ink:#1d1d1f;
    --brand-gray:#5f6063;
    --yellow:#ffe600;
    --slate:#56748f;
    --wood-dark:#3a2412;
    --wood-mid:#9a5a22;
    --wood-light:#d79a4c;
    --mist:#e9edf1;
  }
  *{margin:0;padding:0;box-sizing:border-box}
  html,body{width:1200px;height:1200px;overflow:hidden}
  body{background:var(--navy);font-family:'Poppins',sans-serif;color:var(--ink);position:relative}
  .flyer{position:absolute;left:211px;top:96px;width:786px;height:1018px;background:var(--paper);overflow:hidden}

  .brand{position:absolute;left:0;right:0;top:50px;text-align:center;color:var(--brand-gray);font-weight:600}
  .brand-name{font-size:56px;line-height:1;letter-spacing:4px}
  .brand-tag{margin-top:14px;font-size:21px;letter-spacing:16px;padding-left:16px}

  .hero-photo{position:absolute;left:15px;top:191px;width:757px;height:504px;
    background:radial-gradient(ellipse at 55% 40%,#f0c27a 0%,var(--wood-light) 18%,var(--wood-mid) 45%,var(--wood-dark) 85%)}

  .lower-backdrop{position:absolute;left:0;top:695px;width:786px;height:323px;
    background:linear-gradient(180deg,#f6f7f9 0%,var(--mist) 60%,#dfe4ea 100%)}

  .headline-box{position:absolute;left:39px;top:452px;width:345px;height:349px;
    background:linear-gradient(180deg,rgba(255,230,0,.82) 0%,rgba(255,230,0,.9) 55%,var(--yellow) 100%)}
  .headline{position:absolute;left:28px;top:40px;line-height:1.05}
  .headline .lead{font-size:28px;font-weight:600;letter-spacing:-.3px}
  .headline .big{font-size:44px;font-weight:700;letter-spacing:-.5px;margin-top:6px}
  .headline .mid{font-size:30px;font-weight:600;margin-top:2px;line-height:1.3}
  .headline .mid:first-of-type{margin-top:8px}
  .headline .small{font-size:20px;font-weight:600;letter-spacing:5px;margin-top:10px}

  .accent-line{position:absolute;left:0;top:0;width:786px;height:1018px;pointer-events:none}

  .thumb{position:absolute;top:726px;height:80px}
  .thumb-bar{left:311px;width:154px;clip-path:polygon(50px 0,100% 0,100% 100%,0 100%);
    background:linear-gradient(160deg,#8d9aa8,#cfd5db 45%,#4a4f55)}
  .thumb-taps{left:470px;width:144px;background:linear-gradient(180deg,#6e7d8d,#a47a3f 55%,#c9cccf)}
  .thumb-tanks{left:620px;width:151px;background:linear-gradient(120deg,#cfd3d6,#8a9096 50%,#e1e4e6)}

  .mission{position:absolute;left:0;top:842px;width:786px;height:103px;background:var(--slate)}
  .mission p{position:absolute;left:61px;top:10px;width:660px;color:#fff;font-size:12.6px;font-weight:500;line-height:22.5px;letter-spacing:-.1px}
  .mission-corner{position:absolute;right:0;top:0}

  .contact{position:absolute;left:0;top:954px;width:786px;height:60px}
  .contact-item{position:absolute;top:10px;display:flex;align-items:center;gap:9px;font-weight:600}
  .contact-phone{left:73px;font-size:29px;letter-spacing:-.5px}
  .contact-web{left:355px;font-size:26px;font-weight:500}
  .divider{position:absolute;left:332px;top:10px;width:2px;height:30px;background:var(--ink)}
</style>
</head>
<body>
  <main class="flyer">
    <header class="brand">
      <div class="brand-name">LARKMEAD</div>
      <div class="brand-tag">DESIGN + BUILD</div>
    </header>

    <div class="hero-photo" role="img" aria-label="Photo of a finished brewery taproom with timber ceiling, hanging bulb lights, skylights and long wooden tables"></div>
    <div class="lower-backdrop" role="img" aria-label="Faded photo of a bright restaurant interior"></div>

    <section class="headline-box">
      <div class="headline">
        <div class="lead">Serving all of your</div>
        <div class="big">General<br>Contracting,</div>
        <div class="mid">Construction<br>Management &amp;</div>
        <div class="small">Design needs.</div>
      </div>
    </section>

    <div class="thumb thumb-bar" role="img" aria-label="Photo of a bar counter with wood wall feature"></div>
    <div class="thumb thumb-taps" role="img" aria-label="Photo of a row of beer taps"></div>
    <div class="thumb thumb-tanks" role="img" aria-label="Photo of stainless steel brewing tanks"></div>

    <svg class="accent-line" viewBox="0 0 786 1018" aria-hidden="true">
      <line x1="397" y1="710" x2="287" y2="815" stroke="#1d1d1f" stroke-width="1.6"/>
    </svg>

    <section class="mission">
      <p>Larkmead Design Build, Inc. is dedicated to provide reliable General Contracting services, the highest quality Design Builds and thorough Project Management. Our mission is to build relationships through open and honest communication which has resulted in 95% of our business to be referral or return clients.</p>
      <svg class="mission-corner" width="66" height="103" viewBox="0 0 66 103" aria-hidden="true">
        <polygon points="66,0 66,103 0,103" fill="#ffe600"/>
      </svg>
    </section>

    <footer class="contact">
      <div class="contact-item contact-phone">
        <svg width="27" height="27" viewBox="0 0 24 24" aria-hidden="true">
          <circle cx="12" cy="12" r="12" fill="#1d1d1f"/>
          <path d="M9.2 6.5l1.3 2.6-1 1.1c.6 1.5 1.8 2.7 3.3 3.3l1.1-1 2.6 1.3-.4 2.2c-4.6.2-8.9-4.1-8.7-8.7z" fill="#ffe600"/>
        </svg>
        <span>1110-482-307</span>
      </div>
      <div class="divider"></div>
      <div class="contact-item contact-web">
        <svg width="26" height="26" viewBox="0 0 24 24" aria-hidden="true">
          <circle cx="12" cy="12" r="12" fill="#1d1d1f"/>
          <circle cx="12" cy="12" r="7.5" fill="none" stroke="#ffe600" stroke-width="1.4"/>
          <ellipse cx="12" cy="12" rx="3.2" ry="7.5" fill="none" stroke="#ffe600" stroke-width="1.4"/>
          <line x1="4.5" y1="12" x2="19.5" y2="12" stroke="#ffe600" stroke-width="1.4"/>
        </svg>
        <span>www.larkmeadbuild.com</span>
      </div>
    </footer>
  </main>
</body>
</html>
```